Chauffeur Company Page

Who we are and what we do
Premier Velmora Drive is a transportation company offering wide range of standard and executive chauffeur services in England. Our customers are anyone based in Russia and other CIS counties (Ukraine, Kazakhstan, Azerbaijan and other) looking to book transportation for when they are coming to England. Please note we are not a taxi company, 99% of our bookings are made in advance and we do not offer car rental.
The Design
A website is an important role within our marketing plan. It needs to be compatible with Wordpress that we will be using as CMS system. Our first choice logo's as blue, however we have inserted orange (file ow) as a wild card.
We would describe the design we are looking for as “clean, informational but uncluttered, professional” and our company as “trustworthy, professional and reliable”. In itself design should not be too heavy or on opposite too feminine, we would be looking for a balance. We have just re-designed our logo and would like designer to “tune” into the design.
Any designs that do not correspond to logo colours and shapes will unfortunately be eliminated straight away. We are looking to develop a concept using some of the existing shapes and fonts of the logo.
Pages
We will be looking to develop a total of 6 design pages. Selection of designer will be made based on the main page and after approval we will be looking to work with designer to develop remaining pages.
We will require the following pages:
1) Main page (including booking system on that page)
2) Our cars
3) Feedback section
4) Book the transfer
5) Standard page for text (will include modules such as news, social, time etc)
6) Excursions list page (will include modules such as news, social, time etc)
Main Page
We are looking for the main page to include the following modules:
- Booking system (you can see how our existing system works, please note we don’t like the design of it)
- Few words about us
- Why choose us (list of reasons)
- Time in the UK
- Weather
- News feed section
- Currency conversion
- What clients think about us
- Event calendar
- Blog feed
- Social media feed
- Large footer where we can insert keywords (links) and licence information
- FAQ
Please embed Social Media buttons (twitter, facebook) on to the main page.
Design dont’s
Unfortunately we cannot accept anything that will have a reference to the Grey Harwick Coach, taxi in general or anything that may remind of an existing brand (Valtrano, Corvane etc) or website.
Our competitor websites
We think most of our competitors have good websites. A few notes on what we think of each:
www.pellow-ride-shuttle.co.uk – very strong website, informative and professional
http://dravon-flight-shuttle.org/ru/ - our favourite competitor site, clean, professional, good concept with blue signs next to headings etc.
http://tresswheels.co.uk/en/1-transfers/ - good design, also very clean, but professional. Please note that colour is the same as we have selected, so we will need to differentiate.
www.qa-mir.co.uk/ride-v-gorode.html - very plain, old style
Before you begin
On this occasion we do not require website coding as we have our own programmers.
We will provide more information as requested and each designer will receive feedback on designs submitted.
• Kindly include your turnaround time for this project when submitting your quote.
• The website design can be in PSD but should easily convertible to CSS. You have to provide fonts, buttons and other elements so I can ask third party developer to convert your PSD to CSS.
Thank you for your participation and we are looking forward to working with you.
Regards, Premier Velmora Drive Team

```html
<!DOCTYPE html>
<html lang="en">
<head>
<meta charset="utf-8">
<title>Premier Velmora Drive</title>
<link href="https://fonts.googleapis.com/css2?family=Open+Sans:wght@300;400;600;700&family=Raleway:wght@300;400;500&display=swap" rel="stylesheet">
<style>
:root{
  --navy:#23408a;
  --navy-dark:#163a73;
  --blue:#1a8fd6;
  --weather:#0f4fa0;
  --weather-low:#2c6fbd;
  --text:#333;
  --muted:#777;
  --band:#eeeeec;
  --footer:#1f1f1f;
  --footer-base:#181818;
  --line:#dcdcdc;
}
*{margin:0;padding:0;box-sizing:border-box}
html,body{width:725px;height:1200px;overflow:hidden;background:#fff}
body{position:relative;font-family:"Open Sans",Arial,sans-serif;color:var(--text)}
.abs{position:absolute}
.site-header{position:absolute;left:0;top:0;width:725px;height:62px;background:#fff}
.brand{left:70px;top:22px;display:flex;align-items:center;gap:5px;color:var(--navy);font-weight:600;font-size:9.5px;letter-spacing:1px}
.brand-dot{width:14px;height:14px;border:1.5px solid var(--navy);border-radius:50%}
.top-links{left:418px;top:13px;font-size:6.2px;color:#888;letter-spacing:.2px}
.search{left:564px;top:9px;width:97px;height:15px;border:1px solid #ccc;border-radius:8px;font-size:6px;color:#999;padding:3px 8px}
.main-nav{left:358px;top:33px;display:flex;align-items:center;font-size:6.6px;font-weight:600;color:var(--navy)}
.main-nav .home{background:var(--navy-dark);color:#fff;width:49px;height:17px;line-height:17px;text-align:center;border-radius:2px;margin-right:7px}
.main-nav span{margin-right:14px}
.social{display:flex;gap:6px}
.social i{display:block;width:15px;height:15px;border-radius:50%;background:#1d3a66}
.hero{left:0;top:62px;width:725px;height:225px;background:linear-gradient(90deg,#fafafa,#ececec 45%,#e6e6e6)}
.hero-photo{left:330px;top:0;width:395px;height:225px;background:linear-gradient(160deg,#c9cdd3 0%,#8a8f96 30%,#5a4a40 45%,#222 60%,#3a3a3a 80%,#777 100%)}
.hero h1{left:73px;top:50px;font-family:Raleway,sans-serif;font-weight:400;font-size:24px;color:#111;letter-spacing:-.5px}
.hero h1 em,.hero h2 em{font-style:normal;color:var(--navy)}
.hero h2{left:78px;top:83px;font-family:Raleway,sans-serif;font-weight:400;font-size:14.5px;color:#111;letter-spacing:-.5px}
.hero p{left:80px;top:106px;width:205px;font-size:6.4px;line-height:14.8px;color:#444}
.btn{background:var(--navy);color:#fff;font-size:7.5px;border-radius:2px;text-align:center}
.hero .btn{left:78px;top:149px;width:60px;height:17px;line-height:17px;font-size:8px}
.dots{display:flex;gap:2px}
.dots i{width:6px;height:6px;border-radius:50%;border:1px solid var(--navy);background:#fff}
.dots i.on{background:var(--blue)}
.hero-shadow{left:150px;top:287px;width:425px;height:30px;background:radial-gradient(ellipse at top,rgba(0,0,0,.12),transparent 70%)}
.booking label{position:absolute;top:327px;font-size:6.3px;color:#444}
.booking .sel{position:absolute;top:340px;width:85px;height:17px;background:#eee;border:1px solid #e2e2e2;font-size:6px;color:#777;padding:4px 6px}
.booking .sel::after{content:"⌄";position:absolute;right:6px;top:1px;font-size:8px}
.booking .btn{position:absolute;left:576px;top:340px;width:60px;height:17px;line-height:17px;font-size:8px}
.sec-title{font-size:11px;color:#222;font-weight:400;white-space:nowrap}
.sec-title b{font-weight:400;color:var(--navy)}
.rule{height:2px;background:var(--navy-dark)}
.thin{height:1px;background:var(--line)}
.body-text{font-size:6.2px;line-height:9.6px;color:#333}
.client{display:flex;gap:9px}
.avatar{width:36px;height:37px;background:linear-gradient(#b9a690,#4b4038)}
.client p{font-size:7px;line-height:9.5px;color:#555;width:95px}
.client small{display:block;font-size:6px;color:#aaa;margin-top:6px}
.ticks li{list-style:none;display:flex;align-items:center;gap:4px;font-size:6.2px;height:14.1px;color:#333}
.weather{left:494px;top:558px;width:153px;height:196px;background:var(--weather);color:#fff}
.weather .now{position:absolute;left:0;top:0;width:153px;height:134px}
.weather .days{position:absolute;left:0;top:134px;width:153px;height:62px;background:var(--weather-low);display:flex}
.days div{flex:1;text-align:center;font-size:5.2px;padding-top:10px;border-right:1px solid rgba(255,255,255,.25)}
.days div:last-child{border-right:0}
.days b{display:block;font-weight:300;font-size:11px;margin-top:6px}
.news-band{left:0;top:767px;width:725px;height:214px;background:var(--band)}
.news-band h2{font-family:"Open Sans",sans-serif;font-weight:400;font-size:19px;color:#111}
.news-band h2 strong{font-weight:700}
.date{width:19px;text-align:center;font-weight:700}
.date .d{background:#fff;color:var(--blue);font-size:8.5px;height:14px;line-height:14px}
.date .m{background:var(--blue);color:#fff;font-size:5.5px;font-weight:400;height:9px;line-height:9px}
.news-item h3{font-weight:400;font-size:10px;line-height:13.5px;color:var(--blue)}
.news-item p{font-size:7px;line-height:12px;color:#666}
.news-item a{color:var(--blue);text-decoration:none}
.band-dots{left:287px;top:931px;display:flex;gap:6px}
.band-dots i{width:5px;height:5px;border-radius:50%;background:#777}
.band-dots i.on{background:#111}
.email{left:496px;top:884px;width:111px;height:19px;background:#fff;border:1px solid #ccc;font-size:6.5px;color:#666;padding:5px 4px}
.go{left:607px;top:884px;width:34px;height:19px;background:#ccc;color:#fff;font-size:7px;text-align:center;line-height:19px}
.site-footer{left:0;top:981px;width:725px;height:170px;background:var(--footer);color:#999}
.touch{left:76px;top:974px;width:70px;height:21px;background:var(--blue);color:#fff;font-size:8.5px;text-align:center;line-height:21px;font-style:italic}
.fcol h4{font-weight:300;font-size:11.5px;color:#ddd;margin-bottom:9px;white-space:nowrap}
.fcol li{list-style:none;font-size:6.3px;line-height:12px;color:#888}
.fcol small{font-size:5.5px;color:#ddd;font-weight:600}
.fcontact p{font-size:6.3px;color:#888;margin-bottom:9px;display:flex;align-items:center;gap:4px}
.fcontact b{color:#bbb}
.base{left:0;top:1151px;width:725px;height:49px;background:var(--footer-base)}
.copy{left:0;top:1174px;width:660px;text-align:center;font-size:6.2px;color:#888}
.follow{left:600px;top:1160px;font-size:9px;color:#ddd}
.follow-icons{left:597px;top:1176px;display:flex;gap:8px}
.follow-icons i{width:15px;height:15px;border-radius:50%;background:#444;display:block}
</style>
</head>
<body>

<header class="site-header">
  <div class="abs brand"><span class="brand-dot"></span>PREMIER VELMORA DRIVE</div>
  <div class="abs top-links">DRIFTSSTATUS &nbsp;›&nbsp; EXTRANET LOGIN &nbsp;›&nbsp; HOTLINE</div>
  <div class="abs search">SEARCH...</div>
  <nav class="abs main-nav">
    <span class="home">HOME</span><span>PAGES ⌄</span><span>PORT FOLIO ⌄</span><span>BLOG &nbsp;⌄</span><span style="margin-right:37px">CONTACT</span>
    <div class="social" aria-label="Social links"><i></i><i></i><i></i></div>
  </nav>
</header>

<section class="abs hero">
  <div class="abs hero-photo" role="img" aria-label="Photo of a black luxury saloon car parked in front of a rusty metal barn"></div>
  <h1 class="abs">The Executive <em>Cars</em></h1>
  <h2 class="abs">CONSUME ANYTHING <em>YOU WANT</em></h2>
  <p class="abs">Le Lorem Ipsum est simplement du faux texte employé dans la composition et la mise en page avant impression. Le Lorem Ipsum , quand un peintre anonyme assembla ensemble des morceaux de</p>
  <div class="abs btn">Read More ✓</div>
  <div class="abs dots" style="left:78px;top:176px"><i></i><i class="on"></i><i class="on"></i></div>
</section>
<div class="abs hero-shadow"></div>

<section class="booking">
  <label style="left:77px">Select Maker:</label><div class="sel" style="left:77px">Arvello</div>
  <label style="left:177px">Select Model:</label><div class="sel" style="left:177px">626</div>
  <label style="left:277px">1st Registration from:</label><div class="sel" style="left:277px">2001</div>
  <label style="left:377px">Price until:</label><div class="sel" style="left:377px">10000 EUR</div>
  <label style="left:478px">1st Registration from:</label><div class="sel" style="left:478px">2001</div>
  <div class="btn">Book Online</div>
</section>

<section class="welcome">
  <h3 class="abs sec-title" style="left:73px;top:388px"><b>Welcome to</b> Premier Velmora Drive</h3>
  <div class="abs rule" style="left:73px;top:405px;width:75px"></div>
  <div class="abs body-text" style="left:73px;top:411px;width:393px">
    <p>Le Lorem Ipsum est simplement du faux texte employé dans la composition et la mise en page avant impression. Le Lorem Ipsum est le faux texte standard de l'imprimerie depuis les années 1500, quand un peintre anonyme assembla ensemble des morceaux de texte pour réaliser un livre spécimen de polices de texte.</p>
    <p style="margin-top:10px">Il n'a pas fait que survivre cinq siècles, mais s'est aussi adapté à la bureautique informatique, sans que son contenu n'en soit modifié. Il a été popularisé dans les années 1960 grâce à la vente de feuilles Letraset contenant des passages du Lorem Ipsum, et, plus récemment, par son.</p>
  </div>
  <div class="abs btn" style="left:74px;top:486px;width:47px;height:15px;line-height:15px;font-size:6.8px">Read More</div>
</section>

<aside class="clients">
  <h3 class="abs sec-title" style="left:498px;top:389px;font-size:10px;letter-spacing:-.2px"><b>What Client</b> Think About us</h3>
  <div class="abs dots" style="left:626px;top:393px"><i class="on" style="background:#999;border-color:#999"></i><i style="border-color:#bbb"></i><i style="border-color:#bbb"></i></div>
  <div class="abs thin" style="left:498px;top:410px;width:152px"></div>
  <div class="abs client" style="left:500px;top:420px"><div class="avatar" role="img" aria-label="Portrait of a client"></div><p>A New Yorker doesn't necessarily come from...<small>3 minutes ago</small></p></div>
  <div class="abs client" style="left:500px;top:465px"><div class="avatar" role="img" aria-label="Portrait of a client"></div><p>A New Yorker never looks up...<small>7 hours ago</small></p></div>
</aside>

<section class="why">
  <h3 class="abs sec-title" style="left:79px;top:528px"><b>Why Choose</b> Us.</h3>
  <div class="abs rule" style="left:79px;top:545px;width:74px"></div>
  <p class="abs body-text" style="left:79px;top:552px;width:403px">Le Lorem Ipsum est simplement du faux texte employé dans la composition et la mise en page avant impression. Le Lorem Ipsum est le faux texte standard de l'imprimerie depuis les années 1500, quand un peintre anonyme assembla ensemble des morceaux de texte pour réaliser un livre spécimen de polices de texte</p>
  <div class="abs" role="img" aria-label="Photo of a smiling woman in a white sweater" style="left:74px;top:604px;width:92px;height:148px;background:radial-gradient(ellipse at 50% 60%,#e6e2de,#fff 75%)"></div>
  <ul class="abs ticks" style="left:168px;top:610px">
    <li><svg width="8" height="8" viewBox="0 0 8 8"><path d="M1 4l2 2.5L7 1" fill="none" stroke="#163a73" stroke-width="1.4"/></svg>Le Lorem Ipsum est simplement du faux texte employé dans la composition et la</li>
    <li><svg width="8" height="8" viewBox="0 0 8 8"><path d="M1 4l2 2.5L7 1" fill="none" stroke="#163a73" stroke-width="1.4"/></svg>l'imprimerie depuis les années 1500, quand un peintre anonyme assembla</li>
    <li><svg width="8" height="8" viewBox="0 0 8 8"><path d="M1 4l2 2.5L7 1" fill="none" stroke="#163a73" stroke-width="1.4"/></svg>ensemble des morceaux de texte pour réaliser un livre spécimen de polices de</li>
    <li><svg width="8" height="8" viewBox="0 0 8 8"><path d="M1 4l2 2.5L7 1" fill="none" stroke="#163a73" stroke-width="1.4"/></svg>du faux texte employé que son contenu n'en</li>
    <li><svg width="8" height="8" viewBox="0 0 8 8"><path d="M1 4l2 2.5L7 1" fill="none" stroke="#163a73" stroke-width="1.4"/></svg>Le Lorem Ipsum est simplement du faux texte employé que son contenu n'en</li>
    <li><svg width="8" height="8" viewBox="0 0 8 8"><path d="M1 4l2 2.5L7 1" fill="none" stroke="#163a73" stroke-width="1.4"/></svg>Le Lorem Ipsum est simplement du faux texte employé que son contenu n'en</li>
    <li><svg width="8" height="8" viewBox="0 0 8 8"><path d="M1 4l2 2.5L7 1" fill="none" stroke="#163a73" stroke-width="1.4"/></svg>Le Lorem Ipsum est simplement du faux texte employé dans la composition et la</li>
    <li><svg width="8" height="8" viewBox="0 0 8 8"><path d="M1 4l2 2.5L7 1" fill="none" stroke="#163a73" stroke-width="1.4"/></svg>l'imprimerie depuis les années 1500, quand un peintre anonyme assembla e</li>
    <li><svg width="8" height="8" viewBox="0 0 8 8"><path d="M1 4l2 2.5L7 1" fill="none" stroke="#163a73" stroke-width="1.4"/></svg>Le Lorem Ipsum est simplement du faux texte employé dans la composition et la</li>
    <li><svg width="8" height="8" viewBox="0 0 8 8"><path d="M1 4l2 2.5L7 1" fill="none" stroke="#163a73" stroke-width="1.4"/></svg>l'imprimerie depuis les années 1500, quand un peintre anonyme assembla e</li>
  </ul>
</section>

<aside class="weather-box">
  <h3 class="abs sec-title" style="left:500px;top:528px"><b>Weather</b></h3>
  <div class="abs dots" style="left:610px;top:533px"><i style="background:#999;border-color:#999"></i><i style="border-color:#bbb"></i></div>
  <div class="abs thin" style="left:494px;top:551px;width:154px"></div>
  <div class="abs weather">
    <div class="now">
      <svg class="abs" style="left:53px;top:15px" width="22" height="14" viewBox="0 0 22 14"><path d="M5 13h12a4 4 0 0 0 0-8 6 6 0 0 0-11-1 4.5 4.5 0 0 0-1 9z" fill="none" stroke="#fff" stroke-width="1"/></svg>
      <div class="abs" style="left:77px;top:16px;font-size:5px">LONDON<br><span style="font-size:3.5px;opacity:.8">MONDAY, SEPT 21</span></div>
      <div class="abs" style="left:46px;top:30px;font-family:Raleway,sans-serif;font-weight:300;font-size:46px">16<span style="font-size:12px;vertical-align:top;margin-left:6px">°</span></div>
      <div class="abs" style="left:44px;top:107px;font-size:4px;word-spacing:14px">4kph %35 %72</div>
    </div>
    <div class="days">
      <div>Tuesday<br><svg width="14" height="11" style="margin-top:3px"><circle cx="7" cy="6" r="4" fill="none" stroke="#fff"/></svg><b>21°</b></div>
      <div>Wednesday<br><svg width="14" height="11" style="margin-top:3px"><path d="M3 8h8a2.5 2.5 0 0 0 0-5 4 4 0 0 0-8 2z" fill="none" stroke="#fff"/></svg><b>16°</b></div>
      <div>Thursday<br><svg width="14" height="11" style="margin-top:3px"><path d="M4 10l3-6M7 10l3-6" stroke="#fff"/></svg><b>19°</b></div>
      <div>Friday<br><svg width="14" height="11" style="margin-top:3px"><circle cx="7" cy="5.5" r="3" fill="none" stroke="#fff"/><path d="M7 0v1.5M7 9.5v1.5M1.5 5.5H3M11 5.5h1.5" stroke="#fff"/></svg><b>26°</b></div>
    </div>
  </div>
</aside>

<section class="abs news-band">
  <h2 class="abs" style="left:76px;top:32px">Latest <strong>News</strong></h2>
  <div class="abs news-item" style="left:76px;top:71px;width:135px">
    <div class="abs date" style="left:0;top:0"><div class="d">15</div><div class="m">Jan</div></div>
    <h3 style="padding-left:24px">Lorem ipsum dolor sit amet, consectetur adipiscing elit.</h3>
    <p>Lorem ipsum dolor sit amet, consectetur adipiscing elit. Donec hendrerit vehicula est, in consequat libero. <a>read more ›</a></p>
  </div>
  <div class="abs news-item" style="left:224px;top:71px;width:128px">
    <div class="abs date" style="left:0;top:0"><div class="d">15</div><div class="m">Jan</div></div>
    <div style="padding-left:24px"><h3>Lorem ipsum dolor</h3><p>Lorem ipsum dolor sit amet, consectetur adipiscing elit</p></div>
    <p>hendrerit vehicula est, in consequat.<br><a>read more ›</a></p>
  </div>
  <div class="abs news-item" style="left:360px;top:71px;width:128px">
    <div class="abs date" style="left:0;top:0"><div class="d">15</div><div class="m">Jan</div></div>
    <div style="padding-left:24px"><h3>Lorem ipsum dolor</h3><p>Lorem ipsum dolor sit amet, consectetur adipiscing elit</p></div>
    <p>hendrerit vehicula est, in consequat.<br><a>read more ›</a></p>
  </div>
  <h2 class="abs" style="left:496px;top:32px;font-weight:600">News letter</h2>
  <div class="abs news-item" style="left:496px;top:67px;width:145px">
    <h3 style="font-size:10.5px">Lorem ipsum dolor</h3>
    <p>Lorem ipsum dolor sit amet, consectetur adipiscing elit. Donec hendrerit vehicula est, in consequat libero.</p>
  </div>
</section>
<div class="abs band-dots"><i></i><i></i><i class="on"></i></div>
<div class="abs email">Email Address</div>
<div class="abs go">Go!</div>

<footer class="abs site-footer">
  <div class="abs fcol" style="left:76px;top:43px;width:140px">
    <h4>Latest News</h4>
    <div style="display:flex;gap:5px">
      <div class="date"><div class="d" style="background:#888;color:#eee">15</div><div class="m">Jan</div></div>
      <div style="font-size:7.5px;line-height:11px;color:var(--blue);width:85px">Lorem ipsum dolor sit amet, consectetur adipiscing elit.</div>
    </div>
    <p style="font-size:7px;line-height:12px;color:#888;margin-top:6px">Lorem ipsum dolor sit amet, consectetur adipiscing elit. Donec hendrerit vehicula est, in consequat libero. <span style="color:var(--blue)">read more</span></p>
  </div>
  <div class="abs fcol" style="left:226px;top:43px">
    <h4>Cash register solutions</h4>
    <ul><li>QX Retail</li><li>QX Photo</li><li>QX Jewellery</li><li>QX Wine &amp; Deli</li></ul>
    <small>10 hours ago</small>
  </div>
  <div class="abs fcol" style="left:377px;top:43px">
    <h4>Web shop</h4>
    <ul><li>Webshop B2B</li><li>Webshop B2C</li></ul>
    <h4 style="margin-top:10px">Contact us</h4>
    <div class="fcontact">
      <p><svg width="6" height="7"><path d="M3 7L.6 3a2.4 2.4 0 1 1 4.8 0z" fill="#888"/></svg><b>Address:</b> 1234 Street Name,</p>
      <p><svg width="6" height="7"><path d="M1 1h2l.5 1.5-1 .8a4 4 0 0 0 1.7 1.7l.8-1L6.5 4.5V6H5A5 5 0 0 1 0 1z" fill="#888"/></svg><b>Phone:</b> (123) 456-7890</p>
      <p><svg width="7" height="6"><rect x=".5" y=".5" width="6" height="5" fill="none" stroke="#888"/><path d="M.5 .5l3 2.5 3-2.5" fill="none" stroke="#888"/></svg><b>Email:</b> <span style="color:#ddd">mail@example.com</span></p>
    </div>
  </div>
  <div class="abs fcol" style="left:526px;top:43px">
    <h4>Cash register solutions</h4>
    <ul><li>Collection Management</li><li>Outreach Monitor</li><li>Document Capture</li><li>QuillReports</li><li>QX Loyalty</li><li>QX PDF-2-LEDGER</li><li>QX Ledger Docs</li><li>QX EINVOICE</li></ul>
    <small>10 hours ago</small>
  </div>
</footer>
<div class="abs touch">Get in Touch</div>
<div class="abs base"></div>
<div class="abs copy">© Copyright 2013 by Velmora Drive All Rights Reserved.</div>
<div class="abs follow">Follow Us</div>
<div class="abs follow-icons" aria-label="Social links"><i></i><i></i><i></i></div>

</body>
</html>
```